Business Card design for a mobile solutions company

- we are a mobile telecommunications company focusing on mobile content and solutions
- we are based in Malaysia however operate a regional business
- attached is our company logo and current business card design
- please try to incorporate the "cubes" into the design

our company philosophy is dynamic and outgoing. we are a lean team of less than 50, but we have strong roots in the mobile industry in Asia and we like to challenge ourselves by taking on larger projects.

we love joint ventures and working with partners to find the right solutions for our clients

*please feel free to modify our logo (typeface etc)
**we would like to keep the 3 cube design for the logo, but I would love to see different versions of it
Updates

some of the designs are great and I think our logo (especially the typeface used for the words) doesn't look good. please feel free to update the logo but try to keep the cubes, you are free to modify the cubes and update them.

Reason: looking for more design please

Industry/Entity Type

Telecommunications

Font styles to use
Sans Serif

```html
<!DOCTYPE html>
<html lang="en">
<head>
<meta charset="utf-8">
<title>Torva Link – Business Card Options</title>
<link rel="stylesheet" href="https://fonts.googleapis.com/css2?family=Arimo:wght@400;700&display=swap">
<style>
  :root {
    --page: #ffffff;
    --card-edge: #e3e3e3;
    --ink: #222222;
    --ink-soft: #444444;
    --ink-body: #555555;
    --label: #333333;
    --blue: #0a84c9;
    --blue-deep: #0565a8;
    --red: #e0463f;
    --orange: #ee9433;
    --white: #ffffff;
  }
  * { box-sizing: border-box; margin: 0; padding: 0; }
  html, body {
    width: 1200px; height: 852px; overflow: hidden;
    background: var(--page);
    font-family: "Arimo", Arial, sans-serif;
    color: var(--ink);
  }
  .sheet { position: relative; width: 1200px; height: 852px; }
  .option-label {
    position: absolute; left: 32px;
    font-size: 20px; font-weight: 400; color: var(--label);
  }
  .card {
    position: absolute; width: 550px; height: 346px;
    border: 1px solid var(--card-edge); background: var(--white);
    overflow: hidden;
  }
  .brand {
    position: absolute; display: flex; align-items: center; gap: 14px;
  }
  .brand-mark {
    width: 34px; height: 34px; border-radius: 50%; background: var(--blue);
  }
  .brand-name {
    font-weight: 700; font-size: 36px; color: var(--ink); letter-spacing: 0.5px;
  }
  .person-name { font-weight: 700; color: var(--ink-soft); letter-spacing: 0.5px; }
  .person-title { color: var(--ink-soft); }
  .company { font-weight: 700; color: var(--ink-soft); }
  .address { color: var(--ink-body); }

  /* Option 01 */
  .o1-front .brand { left: 50%; top: 50%; transform: translate(-50%, -50%); }
  .o1-back .company { position: absolute; left: 26px; top: 30px; font-size: 19px; }
  .o1-back .address {
    position: absolute; left: 26px; top: 66px; width: 270px;
    font-size: 13.5px; line-height: 21px;
  }
  .o1-back .artwork { position: absolute; left: 0; top: 0; }
  .o1-back .identity {
    position: absolute; left: 302px; top: 97px; width: 248px; text-align: center;
  }
  .o1-back .identity .person-name { color: var(--white); font-size: 18px; }
  .o1-back .identity .person-title { color: var(--white); font-size: 12.5px; margin-top: 4px; }

  /* Option 02 */
  .o2-front .identity { position: absolute; left: 26px; top: 68px; }
  .o2-front .identity .person-name { font-size: 18px; }
  .o2-front .identity .person-title { font-size: 12.5px; margin-top: 4px; }
  .o2-front .brand { left: 230px; top: 62px; }
  .o2-front .company {
    position: absolute; right: 42px; top: 218px; font-size: 19px;
  }
  .o2-front .address {
    position: absolute; left: 33px; top: 258px;
    font-size: 15px; line-height: 22px;
  }
  .o2-back .pattern {
    position: absolute; inset: 0;
    background: linear-gradient(135deg, var(--blue) 0%, var(--red) 50%, var(--orange) 100%);
  }
  .o2-back .brand-name {
    position: absolute; left: 0; right: 0; top: 148px; text-align: center;
    color: var(--white); font-size: 50px;
  }
</style>
</head>
<body>
<main class="sheet">
  <h2 class="option-label" style="top:20px">Option-01</h2>

  <section class="card o1-front" style="left:29px; top:56px">
    <div class="brand">
      <span class="brand-mark"></span>
      <span class="brand-name">TORVA LINK</span>
    </div>
  </section>

  <section class="card o1-back" style="left:622px; top:56px">
    <svg class="artwork" width="550" height="346" viewBox="0 0 550 346" role="img" aria-label="Large stacked cube artwork in brand blue, red and orange">
      <defs>
        <linearGradient id="blueBlock" x1="0" y1="0" x2="0" y2="1">
          <stop offset="0" stop-color="var(--blue-deep)"/>
          <stop offset="1" stop-color="var(--blue)"/>
        </linearGradient>
        <linearGradient id="warmBlock" x1="0" y1="0" x2="1" y2="0">
          <stop offset="0" stop-color="var(--red)"/>
          <stop offset="0.6" stop-color="var(--red)"/>
          <stop offset="0.62" stop-color="var(--orange)"/>
          <stop offset="1" stop-color="var(--orange)"/>
        </linearGradient>
      </defs>
      <rect x="172" y="180" width="378" height="166" fill="url(#warmBlock)"/>
      <rect x="302" y="0" width="248" height="214" fill="url(#blueBlock)"/>
    </svg>
    <h3 class="company">Torva Link SDN BHD</h3>
    <p class="address">
      Unit 5-4, Level 5 Block 2<br>
      The Meridian Park, North No.12<br>
      Jalan Seroja - 50400,<br>
      Kuala Lumpur, Fax: +60 3 555 0192<br>
      Ph.: +60 12 555 0148, Email:<br>
      elias@torvalink.com.my
    </p>
    <div class="identity">
      <p class="person-name">ELIAS TAN</p>
      <p class="person-title">Chief Marketing Officer</p>
    </div>
  </section>

  <h2 class="option-label" style="top:442px">Option-02</h2>

  <section class="card o2-front" style="left:29px; top:479px">
    <div class="identity">
      <p class="person-name">ELIAS TAN</p>
      <p class="person-title">Chief Marketing Officer</p>
    </div>
    <div class="brand">
      <span class="brand-mark"></span>
      <span class="brand-name">TORVA LINK</span>
    </div>
    <h3 class="company">Torva Link SDN BHD</h3>
    <p class="address">
      Unit 5-4, Level 5 Block 2, The Meridian Park, North No.12<br>
      Jalan Seroja - 50400, Kuala Lumpur, Fax: +60 3 555 0192<br>
      Ph.: +60 12 555 0148, Email: elias@torvalink.com.my
    </p>
  </section>

  <section class="card o2-back" style="left:622px; top:479px">
    <div class="pattern" role="img" aria-label="Repeating cube pattern in blue, red and orange"></div>
    <span class="brand-name">TORVA LINK</span>
  </section>
</main>
</body>
</html>
```